Radical T-shirt Company Shopify Site

I would like to have a a Shopify site designed (and built) for my new t-shirt company. The company is called Zip Tribe and will feature t-shirt designs focused on different characters doing extreme sports. The brand has a mellow and slightly comical feel. We will feature different artists designs as different collections of the brand.
We do not have a logo yet, but we do have some of the sample designs from the artists that we will be featuring on the site. This will give a feel for the branding and style of the site. As far as colors go, I am not sure if a dark theme or light theme will be best. Please use your best judgement for initial designs. Our t-shirt designs are simple and typically line-art style.
It is important to keep in mind that we have several artists that we will feature and that we want to showcase all of them equally until we can understand which will be most popular. Our sites should speak to audiences of all ages. Light, mellow, and slightly comical describe our brand. The site should catch the audiences eye and allow them to see multiple products so they are more likely to buy multiple products.

Expected deliverables:
1. Zip Tribe Gear website (focused on mobile device viewing)- including landing page, multiple collections, product pages, variable colors and sized for shirts and other products, about page, contact page, cart with upsells, subscription package functionality, mailing list pop-up, chat support widget, promo codes, payment collection via stripe- All features should be tested and functioning properly before launch. The site must also be set up to A/B test different products, variations, and upsells.
2. Zip Nana Website (Focused on mobile site viewing) - Should follow the same branding (with a different logo but in the same coloring and style as the Zip Tribe). This should essentially be a copy of the Zip Tribe website include landing page, multiple collections, product pages, variable colors and sized for shirts and other products, about page, contact page, cart with upsells, subscription package functionality, mailing list pop-up, chat support widget, promo codes, payment collection via stripe- Again, this is a duplicate of the Zip Tribe website, but with a different landing page tuned to Zip Nana gear.
3. Coding and development of these sites - with the input of 20-30 products (images, descriptions, pricing provided)

I will provide:
1. Examples of products to help with branding and design of the site
2. Feedback on the site
3. All product information for addition to the site
4. Shopify and plugin credentials or access as needed
5. Ongoing work if this goes well

Looking forward to seeing everyone's designs!

Target Market(s)

People that would wear shirts with our characters; grandmas, grandpas, moms, dads, kids, pet lovers- pretty much anyone who enjoys a bit of humor and a nice shirt.

Industry/Entity Type

Comical yet high end t-shirts

Coding

Coded - Design and coding required

Font styles to use
Sans Serif

Requirements
Must have
• Mobile device optimized, Collections carousel on landing page, upsells, features, other recent order popups for users viewing the site, mailing list popup, coupon codes
Nice to have
• Elegant yet playful feel, branding that instills trust and a quick buy.

```html
<!DOCTYPE html>
<html lang="en">
<head>
<meta charset="utf-8">
<title>Zip Tribe Gear – Home Screens</title>
<link href="https://fonts.googleapis.com/css2?family=Oswald:wght@400;500&family=Roboto:wght@400;500&display=swap" rel="stylesheet">
<style>
:root{
  --orange:#ff8a00;
  --black:#000;
  --ink:#1a1a1a;
  --white:#fff;
  --board:#f3f3f3;
  --line:#e4e4e4;
  --muted:#777;
  --head:'Oswald',sans-serif;
  --body:'Roboto',sans-serif;
}
*{box-sizing:border-box;margin:0;padding:0}
html,body{width:810px;height:1200px;overflow:hidden;background:var(--board)}
.board{position:absolute;left:0;top:0;width:1569px;height:2324px;transform:scale(.51625);transform-origin:0 0;background:var(--board);font-family:var(--body)}
.abs{position:absolute}

/* splash */
.splash{left:418px;top:60px;width:732px;height:507px;overflow:hidden;box-shadow:0 2px 8px rgba(0,0,0,.15)}
.splash-photo{position:absolute;inset:0;background:linear-gradient(100deg,#7b746b 0%,#5d554b 40%,#3c342c 70%,#27231f 100%)}
.splash-photo::after{content:"";position:absolute;left:0;right:0;bottom:0;height:150px;background:linear-gradient(180deg,rgba(40,35,30,0),#1d1c1e)}
.brand-plate{display:flex;align-items:center;justify-content:center;text-align:center;font-family:var(--head);font-weight:500;line-height:1.05}
.splash .brand-plate{left:67px;top:30px;width:210px;height:200px;border:3px solid var(--white);border-radius:50%;color:var(--white);font-size:38px}
.splash-title{left:67px;top:236px;color:var(--white);font-family:var(--head);font-size:24px;line-height:30px;font-weight:400;letter-spacing:.3px}
.pill{top:315px;height:36px;border-radius:18px;font-family:var(--head);font-size:14px;display:flex;align-items:center;justify-content:center;color:var(--white)}
.pill-solid{left:69px;width:117px;background:var(--orange)}
.pill-ghost{left:195px;width:117px;border:2px solid var(--white)}

/* screen */
.screen{top:620px;width:732px;height:1603px;overflow:hidden;background:var(--white);box-shadow:0 2px 8px rgba(0,0,0,.15)}
.screen-left{left:37px}
.screen-right{left:806px}
.topbar{left:0;top:0;width:732px;height:28px;background:var(--black)}
.social-row{display:flex;gap:4px}
.topbar .social-row{left:68px;top:8px}
.social-dot{width:12px;height:12px;border:1px solid var(--white);border-radius:50%}
.account-links{right:67px;top:8px;display:flex;gap:16px;color:var(--white);font-family:var(--head);font-size:9px;align-items:center}
.account-links span+span::before{content:"|";margin-right:16px}
.navbar{left:0;top:28px;width:732px;height:69px;background:var(--white)}
.nav-links{left:287px;top:29px;display:flex;gap:27px;font-family:var(--head);font-size:10px;color:var(--ink)}
.nav-links .current{color:var(--orange);position:relative}
.nav-links .current::after{content:"";position:absolute;left:-3px;right:-3px;top:22px;height:2px;background:var(--orange)}
.cart{left:625px;top:26px;display:flex;gap:4px;align-items:center;font-family:var(--head);font-size:10px;color:var(--ink)}
.cart-badge{position:absolute;left:8px;top:9px;width:9px;height:9px;border-radius:50%;background:var(--orange)}
.nav-plate{left:68px;top:30px;width:112px;height:112px;border-radius:50%;background:var(--white);color:var(--ink);font-size:19px;z-index:3}

.hero{left:0;top:97px;width:732px;height:443px;background:linear-gradient(90deg,#586673 0%,#6e7c88 45%,#4e5b66 100%)}
.hero-shirt{left:350px;top:80px;width:240px;height:320px;border-radius:40px 40px 8px 8px;background:#1d3038}
.hero-title{left:67px;top:243px;font-family:var(--head);font-weight:500;font-size:40px;color:var(--white);letter-spacing:.5px}
.hero-copy{left:67px;top:298px;width:265px;font-size:11.5px;line-height:19px;color:#eef1f3}
.btn-orange{background:var(--orange);color:var(--white);font-family:var(--head);display:flex;align-items:center;justify-content:center}
.hero-btn{left:67px;top:370px;width:98px;height:34px;font-size:13px}
.dots{left:353px;top:525px;display:flex;gap:5px}
.dots i{width:6px;height:6px;border-radius:50%;background:var(--white)}
.dots i.on{background:var(--orange)}

.section-title{left:0;width:732px;text-align:center;font-family:var(--head);font-weight:500;font-size:24px;color:var(--ink)}
.featured-title{top:565px}
.card{width:191px;height:270px;border:2px solid #efefef;background:var(--white)}
.shirt{left:12px;top:12px;width:150px;height:172px;border-radius:26px 26px 6px 6px}
.tool{width:17px;height:17px;border:1px solid #ddd;left:165px;display:flex;align-items:center;justify-content:center}
.t1{top:152px}.t2{top:173px}.t3{top:195px}
.size-tag{left:97px;top:154px;width:62px;height:15px;border:1px solid #ddd;font-size:6.5px;color:#999;display:flex;align-items:center;justify-content:center;background:var(--white)}
.swatches{left:101px;top:177px;display:flex;gap:3px}
.swatches i{width:6px;height:6px}
.stars{left:0;top:197px;width:191px;text-align:center;color:var(--orange);font-size:9px;letter-spacing:1px}
.card-name{left:0;top:214px;width:191px;text-align:center;font-family:var(--head);font-weight:500;font-size:15px;color:var(--ink)}
.card-price{left:0;top:237px;width:191px;text-align:center;font-family:var(--head);font-size:15px;color:var(--orange)}

.promo{left:0;top:1227px;width:732px;height:140px;background:var(--orange)}
.promo-title{top:26px;color:var(--white)}
.rule{left:350px;width:32px;height:2px}
.promo-input{left:155px;top:78px;width:354px;height:33px;background:var(--white);font-size:9px;color:#555;padding:12px}
.promo-btn{left:509px;top:78px;width:67px;height:33px;background:var(--black);color:var(--white);font-family:var(--head);font-size:12px;display:flex;align-items:center;justify-content:center}

.footer{left:0;top:1367px;width:732px;height:236px;background:var(--black);color:var(--white)}
.foot-head{font-family:var(--head);font-weight:500;font-size:14px}
.field{background:var(--white);height:21px;font-size:7px;color:#666;padding:7px 8px}
.foot-submit{left:70px;top:157px;width:60px;height:21px;font-size:9px}
.info-ico{left:347px;width:26px;height:26px;border:1px solid var(--white);border-radius:50%;display:flex;align-items:center;justify-content:center}
.info-label{left:380px;font-family:var(--head);font-size:12px}
.info-text{left:380px;font-size:8px;line-height:11px;color:#ddd}
.foot-plate{left:527px;top:24px;width:128px;height:118px;border:2px solid var(--white);border-radius:50%;font-size:19px;color:var(--white)}
.footer .social-row{left:527px;top:148px;gap:4px}
.footer .social-dot{width:20px;height:20px}
.chat-tab{left:700px;top:78px;width:32px;height:90px;background:var(--orange);border-radius:4px 0 0 4px;display:flex;align-items:center;justify-content:center}
.chat-tab span{transform:rotate(-90deg);font-family:var(--head);font-size:11px;white-space:nowrap}
.copyright{left:0;top:210px;width:732px;text-align:center;font-family:var(--head);font-size:9px}

/* mailing popup */
.overlay{left:0;top:0;width:732px;height:1603px;background:rgba(0,0,0,.72);z-index:5}
.popup{left:147px;top:210px;width:439px;height:300px;background:var(--white);z-index:6}
.popup .brand-plate{left:150px;top:14px;width:140px;height:120px;border:2px solid var(--ink);border-radius:50%;font-size:22px;color:var(--ink)}
.popup-copy{left:40px;top:147px;width:359px;text-align:center;font-size:9.5px;line-height:16px;color:#333}
.popup-input{left:37px;top:197px;width:302px;height:31px;border:1px solid #ccc;font-size:9px;color:#444;padding:10px}
.popup-btn{left:339px;top:197px;width:62px;height:31px;font-family:var(--body);font-size:9px}
.popup-close{left:562px;top:197px;width:36px;height:36px;border-radius:50%;background:var(--black);border:2px solid var(--white);color:var(--white);font-size:13px;z-index:7;display:flex;align-items:center;justify-content:center;font-family:var(--body);font-weight:500}
</style>
</head>
<body>
<div class="board">

  <!-- Landing splash -->
  <section class="abs splash">
    <div class="splash-photo" role="img" aria-label="Photo of a surfer running into the sea with a board at dusk, water splashing"></div>
    <div class="abs brand-plate">ZIP<br>TRIBE<br>GEAR</div>
    <h1 class="abs splash-title">SED UT PERSPICIATIS UNDE OMNIS<br>ISTE NATUS ERROR SIT VOLUPTATEM</h1>
    <a class="abs pill pill-solid">ZIP TRIBE GEAR</a>
    <a class="abs pill pill-ghost">ZIP NANA</a>
  </section>

  <!-- Home with mailing list popup -->
  <section class="abs screen screen-left">
    <header class="abs topbar">
      <div class="abs social-row"><i class="social-dot"></i><i class="social-dot"></i><i class="social-dot"></i><i class="social-dot"></i><i class="social-dot"></i></div>
      <div class="abs account-links"><span>LOGIN</span><span>REGISTER</span><span>SEARCH</span></div>
    </header>
    <nav class="abs navbar">
      <div class="abs nav-links"><span class="current">HOME</span><span>ABOUT US</span><span>SERVICES</span><span>PRODUCT</span><span>NEWS</span><span>CONTACT US</span></div>
      <div class="abs cart"><svg width="14" height="12" viewBox="0 0 14 12"><path d="M1 1h2l2 7h7l1-5H4" fill="none" stroke="#1a1a1a" stroke-width="1.2"/></svg><span>£0.00</span><i class="cart-badge"></i></div>
    </nav>
    <div class="abs brand-plate nav-plate">ZIP TRIBE<br>GEAR</div>
    <div class="abs hero" role="img" aria-label="Dark t-shirt with line-art surfer print hanging on a painted brick wall">
      <div class="abs hero-shirt"></div>
      <h2 class="abs hero-title">ZIP TRIBE GEAR</h2>
      <p class="abs hero-copy">Sed ut perspiciatis unde omnis iste natus error sit voluptatem accusantium doloremque laudantium, unde omnis totam rem aperiam</p>
      <a class="abs btn-orange hero-btn">READ MORE</a>
      <div class="abs dots"><i></i><i class="on"></i><i></i></div>
    </div>
    <h3 class="abs section-title featured-title">FEATURED PRODUCTS</h3>
    <div class="abs card" style="left:67px;top:620px"><div class="abs shirt" style="background:#f1f1f1" role="img" aria-label="White shirt with line-art print"></div><p class="abs stars">★★★★★</p><p class="abs card-name">PRODUCT NAME</p><p class="abs card-price">$25.99</p></div>
    <div class="abs card" style="left:270px;top:620px"><div class="abs shirt" style="background:#111" role="img" aria-label="Black shirt with line-art print"></div><p class="abs stars">★★★★★</p><p class="abs card-name">PRODUCT NAME</p><p class="abs card-price">$25.99</p></div>
    <div class="abs card" style="left:473px;top:620px"><div class="abs shirt" style="background:#1e78d2" role="img" aria-label="Blue shirt with line-art print"></div><p class="abs stars">★★★★★</p><p class="abs card-name">PRODUCT NAME</p><p class="abs card-price">$25.99</p></div>
    <div class="abs card" style="left:67px;top:913px"><div class="abs shirt" style="background:#2a2d3e" role="img" aria-label="Navy shirt with line-art print"></div><p class="abs stars">★★★★★</p><p class="abs card-name">PRODUCT NAME</p><p class="abs card-price">$25.99</p></div>
    <div class="abs card" style="left:270px;top:913px"><div class="abs shirt" style="background:#9a9a9a" role="img" aria-label="Grey shirt with line-art print"></div><p class="abs stars">★★★★★</p><p class="abs card-name">PRODUCT NAME</p><p class="abs card-price">$25.99</p></div>
    <div class="abs card" style="left:473px;top:913px"><div class="abs shirt" style="background:#d22aa4" role="img" aria-label="Magenta shirt with line-art print"></div><p class="abs stars">★★★★★</p><p class="abs card-name">PRODUCT NAME</p><p class="abs card-price">$25.99</p></div>
    <section class="abs promo">
      <h3 class="abs section-title promo-title">PROMO CODES</h3>
      <i class="abs rule" style="top:64px;background:var(--white)"></i>
      <div class="abs promo-input">Enter Promo Code</div>
      <a class="abs promo-btn">APPLY</a>
    </section>
    <footer class="abs footer">
      <h4 class="abs foot-head" style="left:70px;top:28px">GET IN TOUCH</h4>
      <div class="abs field" style="left:70px;top:65px;width:110px">First Name :</div>
      <div class="abs field" style="left:186px;top:65px;width:110px">Last Name :</div>
      <div class="abs field" style="left:70px;top:92px;width:110px">Email :</div>
      <div class="abs field" style="left:186px;top:92px;width:110px">Phone :</div>
      <div class="abs field" style="left:70px;top:119px;width:226px;height:32px">Message :</div>
      <a class="abs btn-orange foot-submit">SUBMIT</a>
      <h4 class="abs foot-head" style="left:350px;top:28px">CONTACT INFO</h4>
      <div class="abs info-ico" style="top:61px"><svg width="10" height="12" viewBox="0 0 10 12"><path d="M5 11C2 7 1 5.5 1 4a4 4 0 018 0c0 1.5-1 3-4 7z" fill="#fff"/></svg></div>
      <p class="abs info-label" style="top:58px">ADDRESS</p>
      <p class="abs info-text" style="top:75px">Lorem Ipsum 767 Lorem ipsum<br>Loremlp, CA 91790</p>
      <div class="abs info-ico" style="top:110px"><svg width="11" height="11" viewBox="0 0 11 11"><path d="M2 1l2 2-1 1.5c.8 1.6 1.9 2.7 3.5 3.5L8 7l2 2-1.5 1.5C4.5 10 1 6.5.5 2.5z" fill="none" stroke="#fff"/></svg></div>
      <p class="abs info-label" style="top:107px">PHONE</p>
      <p class="abs info-text" style="top:124px">+1 888 888 8888</p>
      <div class="abs info-ico" style="top:150px"><svg width="12" height="9" viewBox="0 0 12 9"><rect x=".5" y=".5" width="11" height="8" fill="none" stroke="#fff"/><path d="M.5.5L6 5l5.5-4.5" fill="none" stroke="#fff"/></svg></div>
      <p class="abs info-label" style="top:147px">EMAIL</p>
      <p class="abs info-text" style="top:164px">hello@ziptribegear.com</p>
      <div class="abs brand-plate foot-plate">ZIP TRIBE<br>GEAR</div>
      <div class="abs social-row"><i class="social-dot"></i><i class="social-dot"></i><i class="social-dot"></i><i class="social-dot"></i><i class="social-dot"></i><i class="social-dot"></i></div>
      <div class="abs chat-tab"><span>LIVE CHAT</span></div>
      <p class="abs copyright">© COPYRIGHT 2022 ZIP TRIBE GEAR.ALL RIGHTS RESERVED.</p>
    </footer>
    <div class="abs overlay"></div>
    <div class="abs popup">
      <div class="abs brand-plate">ZIP TRIBE<br>GEAR</div>
      <p class="abs popup-copy">Sed ut perspiciatis unde omnis iste natus error sit voluptatem accusantium doloremque laudantium, totam rem aperiam</p>
      <div class="abs popup-input">Enter Your Email :</div>
      <a class="abs btn-orange popup-btn">SUBMIT</a>
    </div>
    <div class="abs popup-close">x</div>
  </section>

  <!-- Home -->
  <section class="abs screen screen-right">
    <header class="abs topbar">
      <div class="abs social-row"><i class="social-dot"></i><i class="social-dot"></i><i class="social-dot"></i><i class="social-dot"></i><i class="social-dot"></i></div>
      <div class="abs account-links"><span>LOGIN</span><span>REGISTER</span><span>SEARCH</span></div>
    </header>
    <nav class="abs navbar">
      <div class="abs nav-links"><span class="current">HOME</span><span>ABOUT US</span><span>SERVICES</span><span>PRODUCT</span><span>NEWS</span><span>CONTACT US</span></div>
      <div class="abs cart"><svg width="14" height="12" viewBox="0 0 14 12"><path d="M1 1h2l2 7h7l1-5H4" fill="none" stroke="#1a1a1a" stroke-width="1.2"/></svg><span>£0.00</span><i class="cart-badge"></i></div>
    </nav>
    <div class="abs brand-plate nav-plate">ZIP TRIBE<br>GEAR</div>
    <div class="abs hero" role="img" aria-label="Dark t-shirt with line-art surfer print hanging on a painted brick wall">
      <div class="abs hero-shirt"></div>
      <h2 class="abs hero-title">ZIP TRIBE GEAR</h2>
      <p class="abs hero-copy">Sed ut perspiciatis unde omnis iste natus error sit voluptatem accusantium doloremque laudantium, unde omnis totam rem aperiam</p>
      <a class="abs btn-orange hero-btn">READ MORE</a>
      <div class="abs dots"><i></i><i class="on"></i><i></i></div>
    </div>
    <h3 class="abs section-title featured-title">FEATURED PRODUCTS</h3>

    <div class="abs card" style="left:67px;top:620px">
      <div class="abs shirt" style="background:#f1f1f1" role="img" aria-label="White shirt with line-art print"></div>
      <div class="abs size-tag">Size : S,M,L,XL</div>
      <div class="abs swatches"><i style="background:#ff8a00"></i><i style="background:#111"></i><i style="background:#d22aa4"></i><i style="background:#1e3fd2"></i><i style="background:#e0203a"></i></div>
      <i class="abs tool t1"><svg width="8" height="8"><path d="M1 7L7 1M4 1h3v3" stroke="#333" fill="none"/></svg></i>
      <i class="abs tool t2"><svg width="8" height="8"><path d="M1 7L7 1M4 1h3v3" stroke="#333" fill="none"/></svg></i>
      <i class="abs tool t3"><svg width="8" height="8"><path d="M4 7L1 4a1.5 1.5 0 013-2 1.5 1.5 0 013 2z" stroke="#333" fill="none"/></svg></i>
      <p class="abs stars">★★★★★</p><p class="abs card-name">PRODUCT NAME</p><p class="abs card-price">$25.99</p>
    </div>
    <div class="abs card" style="left:270px;top:620px">
      <div class="abs shirt" style="background:#111" role="img" aria-label="Black shirt with line-art print"></div>
      <i class="abs tool t1"><svg width="8" height="8"><path d="M1 7L7 1M4 1h3v3" stroke="#333" fill="none"/></svg></i>
      <i class="abs tool t2"><svg width="8" height="8"><path d="M1 7L7 1M4 1h3v3" stroke="#333" fill="none"/></svg></i>
      <i class="abs tool t3"><svg width="8" height="8"><path d="M4 7L1 4a1.5 1.5 0 013-2 1.5 1.5 0 013 2z" stroke="#333" fill="none"/></svg></i>
      <p class="abs stars">★★★★★</p><p class="abs card-name">PRODUCT NAME</p><p class="abs card-price">$25.99</p>
    </div>
    <div class="abs card" style="left:473px;top:620px">
      <div class="abs shirt" style="background:#1e78d2" role="img" aria-label="Blue shirt with line-art print"></div>
      <i class="abs tool t1"><svg width="8" height="8"><path d="M1 7L7 1M4 1h3v3" stroke="#333" fill="none"/></svg></i>
      <i class="abs tool t2"><svg width="8" height="8"><path d="M1 7L7 1M4 1h3v3" stroke="#333" fill="none"/></svg></i>
      <i class="abs tool t3"><svg width="8" height="8"><path d="M4 7L1 4a1.5 1.5 0 013-2 1.5 1.5 0 013 2z" stroke="#333" fill="none"/></svg></i>
      <p class="abs stars">★★★★★</p><p class="abs card-name">PRODUCT NAME</p><p class="abs card-price">$25.99</p>
    </div>
    <div class="abs card" style="left:67px;top:913px">
      <div class="abs shirt" style="background:#2a2d3e" role="img" aria-label="Navy shirt with line-art print"></div>
      <i class="abs tool t1"><svg width="8" height="8"><path d="M1 7L7 1M4 1h3v3" stroke="#333" fill="none"/></svg></i>
      <i class="abs tool t2"><svg width="8" height="8"><path d="M1 7L7 1M4 1h3v3" stroke="#333" fill="none"/></svg></i>
      <i class="abs tool t3"><svg width="8" height="8"><path d="M4 7L1 4a1.5 1.5 0 013-2 1.5 1.5 0 013 2z" stroke="#333" fill="none"/></svg></i>
      <p class="abs stars">★★★★★</p><p class="abs card-name">PRODUCT NAME</p><p class="abs card-price">$25.99</p>
    </div>
    <div class="abs card" style="left:270px;top:913px">
      <div class="abs shirt" style="background:#9a9a9a" role="img" aria-label="Grey shirt with line-art print"></div>
      <i class="abs tool t1"><svg width="8" height="8"><path d="M1 7L7 1M4 1h3v3" stroke="#333" fill="none"/></svg></i>
      <i class="abs tool t2"><svg width="8" height="8"><path d="M1 7L7 1M4 1h3v3" stroke="#333" fill="none"/></svg></i>
      <i class="abs tool t3"><svg width="8" height="8"><path d="M4 7L1 4a1.5 1.5 0 013-2 1.5 1.5 0 013 2z" stroke="#333" fill="none"/></svg></i>
      <p class="abs stars">★★★★★</p><p class="abs card-name">PRODUCT NAME</p><p class="abs card-price">$25.99</p>
    </div>
    <div class="abs card" style="left:473px;top:913px">
      <div class="abs shirt" style="background:#d22aa4" role="img" aria-label="Magenta shirt with line-art print"></div>
      <i class="abs tool t1"><svg width="8" height="8"><path d="M1 7L7 1M4 1h3v3" stroke="#333" fill="none"/></svg></i>
      <i class="abs tool t2"><svg width="8" height="8"><path d="M1 7L7 1M4 1h3v3" stroke="#333" fill="none"/></svg></i>
      <i class="abs tool t3"><svg width="8" height="8"><path d="M4 7L1 4a1.5 1.5 0 013-2 1.5 1.5 0 013 2z" stroke="#333" fill="none"/></svg></i>
      <p class="abs stars">★★★★★</p><p class="abs card-name">PRODUCT NAME</p><p class="abs card-price">$25.99</p>
    </div>

    <section class="abs promo">
      <h3 class="abs section-title promo-title">PROMO CODES</h3>
      <i class="abs rule" style="top:64px;background:var(--white)"></i>
      <div class="abs promo-input">Enter Promo Code</div>
      <a class="abs promo-btn">APPLY</a>
    </section>
    <footer class="abs footer">
      <h4 class="abs foot-head" style="left:70px;top:28px">GET IN TOUCH</h4>
      <div class="abs field" style="left:70px;top:65px;width:110px">First Name :</div>
      <div class="abs field" style="left:186px;top:65px;width:110px">Last Name :</div>
      <div class="abs field" style="left:70px;top:92px;width:110px">Email :</div>
      <div class="abs field" style="left:186px;top:92px;width:110px">Phone :</div>
      <div class="abs field" style="left:70px;top:119px;width:226px;height:32px">Message :</div>
      <a class="abs btn-orange foot-submit">SUBMIT</a>
      <h4 class="abs foot-head" style="left:350px;top:28px">CONTACT INFO</h4>
      <div class="abs info-ico" style="top:61px"><svg width="10" height="12" viewBox="0 0 10 12"><path d="M5 11C2 7 1 5.5 1 4a4 4 0 018 0c0 1.5-1 3-4 7z" fill="#fff"/></svg></div>
      <p class="abs info-label" style="top:58px">ADDRESS</p>
      <p class="abs info-text" style="top:75px">Lorem Ipsum 767 Lorem ipsum<br>Loremlp, CA 91790</p>
      <div class="abs info-ico" style="top:110px"><svg width="11" height="11" viewBox="0 0 11 11"><path d="M2 1l2 2-1 1.5c.8 1.6 1.9 2.7 3.5 3.5L8 7l2 2-1.5 1.5C4.5 10 1 6.5.5 2.5z" fill="none" stroke="#fff"/></svg></div>
      <p class="abs info-label" style="top:107px">PHONE</p>
      <p class="abs info-text" style="top:124px">+1 888 888 8888</p>
      <div class="abs info-ico" style="top:150px"><svg width="12" height="9" viewBox="0 0 12 9"><rect x=".5" y=".5" width="11" height="8" fill="none" stroke="#fff"/><path d="M.5.5L6 5l5.5-4.5" fill="none" stroke="#fff"/></svg></div>
      <p class="abs info-label" style="top:147px">EMAIL</p>
      <p class="abs info-text" style="top:164px">hello@ziptribegear.com</p>
      <div class="abs brand-plate foot-plate">ZIP TRIBE<br>GEAR</div>
      <div class="abs social-row"><i class="social-dot"></i><i class="social-dot"></i><i class="social-dot"></i><i class="social-dot"></i><i class="social-dot"></i><i class="social-dot"></i></div>
      <div class="abs chat-tab"><span>LIVE CHAT</span></div>
      <p class="abs copyright">© COPYRIGHT 2022 ZIP TRIBE GEAR.ALL RIGHTS RESERVED.</p>
    </footer>
  </section>

</div>
</body>
</html>
```